Hosvin Logo and business card

We need a business card and logo, we are currently using a logo that we like but would like to be a bit more streamlined. We deal with very high end clients and our business card needs to reflect that. We would love to see and hire somebody that can deliver a very MODERN, simple design. With he main front of the card to be black with either a red lettering or White to provide great contrast. I would like to have a minimalist abstract picture of a heavy machine on it but it is not a requirement ( most likely an Crane ( a brisk otter crane with a bucket would be perfect or maybe a vendrel 820 TX )) If it keeps in line with being a classic simple, and modern design. Letterpress is also an option where it gives it a great look and texture, the card will be printed on a thick stock. On the back there needs to be a star included somewhere on the card and design, this represents the first generation that started the company back in 1936 therefore it is a sentimental addition ( make it modern and simple)
We do not want a cheesy construction template. We do heavy site work, aka we use excavators, payloaders, off road jox m41 trucks, very big fun toys.
There is a huge chance to get the web design as well for the winning design.
Have fun, cannot wait to see the designs!
In addition, we'd like to point out that our primary need and priority is still the BUSINESS CARD design itself. The logo has to complement the overall look of the business card, but it is secondary to the card's look. Please keep this in mind.
Thank you,
Gideon
Target Market(s)
General Contractors, upscale home owners ( house values of 1M plus)
and commercial property owners.
Projects range from $5000 to 1 million.
Industry/Entity Type
Construction
Requirements
Must have
- Star incorporated into design
Nice to have
- an abstract heavy site work machine ( pics attached) If it keeps in line with being a classic simple, and modern design.
I would like to have black and red on the design since all the lettering on the trucks is red, but i will let the designer take care of that.

```html
<!DOCTYPE html>
<html lang="en">
<head>
<meta charset="utf-8">
<title>Hosvin Industries Inc. — Business Card</title>
<link rel="stylesheet" href="https://fonts.googleapis.com/css2?family=Cabin:ital,wght@0,400;0,500;0,600;1,400&display=swap">
<style>
  :root {
    --page: #e9e6e1;
    --card-center: #6d6d6d;
    --card-edge: #3f3f3f;
    --rule: #cfcfcf;
    --ink: #111111;
    --red: #d10a0a;
    --title: #d4d4d4;
    --mark: rgba(160, 40, 40, 0.55);
  }
  * { margin: 0; padding: 0; box-sizing: border-box; }
  html, body { width: 1200px; height: 1000px; overflow: hidden; }
  body {
    background: var(--page);
    font-family: "Cabin", sans-serif;
    position: relative;
  }
  .card {
    position: absolute;
    width: 800px;
    height: 478px;
    background: radial-gradient(ellipse at 55% 50%, var(--card-center) 0%, #5a5a5a 55%, var(--card-edge) 100%);
    box-shadow: 0 4px 10px rgba(0,0,0,0.25);
    overflow: hidden;
  }
  .card--front { left: 30px; top: 20px; }
  .card--back { left: 370px; top: 502px; }
  .card__rules { position: absolute; inset: 0; }
  .card__rules path { fill: none; stroke: var(--rule); stroke-width: 7; stroke-linejoin: round; }

  .brand {
    position: absolute;
    color: var(--red);
    font-weight: 600;
    letter-spacing: 0.04em;
    text-transform: uppercase;
    display: flex;
    align-items: center;
    gap: 12px;
    white-space: nowrap;
  }
  .brand__square { background: var(--red); display: block; }
  .brand--small { left: 92px; top: 44px; font-size: 26px; }
  .brand--small .brand__square { width: 22px; height: 22px; }
  .brand--large { left: 250px; top: 205px; font-size: 40px; }
  .brand--large .brand__square { width: 34px; height: 34px; }

  .corner-mark {
    position: absolute;
    right: 42px;
    bottom: 40px;
    width: 66px;
    height: 66px;
    background: var(--mark);
  }

  .holder { position: absolute; left: 0; right: 0; text-align: center; }
  .holder__name {
    top: 176px;
    font-size: 50px;
    font-weight: 400;
    letter-spacing: 0.06em;
    color: var(--ink);
  }
  .holder__name .accent { color: var(--red); }
  .holder__title {
    top: 240px;
    font-size: 27px;
    font-style: italic;
    letter-spacing: 0.08em;
    color: var(--title);
  }

  .contact { position: absolute; font-size: 18px; line-height: 19px; color: var(--ink); letter-spacing: 0.03em; }
  .contact .accent { color: var(--red); }
  .contact--web { left: 40px; top: 364px; }
  .contact--phone { left: 450px; top: 364px; }
  .contact--address { left: 116px; top: 420px; }

  .back-web {
    position: absolute;
    left: 108px;
    top: 56px;
    font-size: 22px;
    font-weight: 500;
    letter-spacing: 0.05em;
    color: var(--ink);
  }
  .back-web .accent { color: var(--red); }
</style>
</head>
<body>

<section class="card card--front" aria-label="Business card front">
  <svg class="card__rules" width="800" height="478" viewBox="0 0 800 478" aria-hidden="true">
    <path d="M0 114 H398 V18 H800"/>
    <path d="M0 456 H646 V344 H800"/>
  </svg>
  <div class="brand brand--small"><span class="brand__square"></span>Hosvin Industries Inc.</div>
  <p class="holder holder__name">YOUR <span class="accent">NAME</span></p>
  <p class="holder holder__title">GENERAL MANAGER</p>
  <p class="contact contact--web">your_email@<span class="accent">hosvin</span>.com<br>www.<span class="accent">hosvin</span>.com</p>
  <p class="contact contact--phone">P 123-456-7890<br>F 123-456-7890</p>
  <p class="contact contact--address">1234, street_name, city_name, cc 90000</p>
  <span class="corner-mark" aria-hidden="true"></span>
</section>

<section class="card card--back" aria-label="Business card back">
  <svg class="card__rules" width="800" height="478" viewBox="0 0 800 478" aria-hidden="true">
    <path d="M0 136 H392 V0"/>
    <path d="M0 458 H700 V360 H800"/>
  </svg>
  <p class="back-web">www.<span class="accent">hosvin</span>.com</p>
  <div class="brand brand--large"><span class="brand__square"></span>Hosvin Industries Inc.</div>
  <span class="corner-mark" aria-hidden="true"></span>
</section>

</body>
</html>
```